Powerpoint design template for PLAYNOVA for new digital platform

We would like to use a PowerPoint template, we would like to create a new page, we would like to create a new digital platform PLAYNOVA for schools and parents for the creation of playful communication and educational tools for children to enhance their positive development, amaze them learn in a playful way. This platform is going to be the most creative, stimulating and innovative classroom, easy to use and fast to implement. Scrapbooking, collages ... Magazine, newsletters Diplomla / awards Slideshows Facebook Calendars Organizers Greetings Games ... This powerpoint template will be used essential to We are looking for a professional design, positioning our brand in the children market with an adult hearing. so you will need to find a good deal. Primary target: nurseries & schools from 0 to 18 years old and universities (in 2nd phase) Secondary target: small & medium businesses Third target: general public, and TPE If it is a color scheme, then it is suggested that it be marketed in Europe (UK, Italy, Spain) and in a 2nd Stage USA and other countries. multiple options for front page, insidious pages (multiple styles with limited text and extended text) and final contact page We need something to read, we can not do it too much, but we can not do it. , and inside pages aligned to our logo

Target Market(s)

Target 1; Education with teacher Target 2; parents and grandparents

Industry/Entity Type

Education

Font styles to use
Other font styles liked:
• not decided. but not too fancy

Requirements
Must have
• Multi page options for front page, page insides (multiple styles with limited text and extended text) and final page contact
Nice to have
• do not have a lot of ideas. We need something to read, we can not get away from it
Should not have
• not too fancy and busy: keep clarity & simplicity while reassuring on quality

```html
<!DOCTYPE html>
<html lang="en">
<head>
<meta charset="utf-8">
<title>Playnova – Investment opportunity</title>
<link rel="stylesheet" href="https://fonts.googleapis.com/css2?family=Carlito:ital@1&family=Open+Sans:wght@400;700&display=swap">
<style>
  :root {
    --page: #ffffff;
    --text: #5c5c5c;
    --title: #6a6a6a;
    --teal: #4fb3a4;
    --lime: #d9e055;
    --screen-light: #e4e4e4;
    --screen-dark: #a9a9a9;
  }
  html, body {
    margin: 0;
    padding: 0;
    overflow: hidden;
    background: var(--page);
  }
  .slide {
    position: relative;
    width: 1200px;
    height: 676px;
    overflow: hidden;
    background: var(--page);
    font-family: "Open Sans", Arial, sans-serif;
    color: var(--text);
  }
  .title-bar {
    position: absolute;
    left: 40px;
    top: 40px;
    width: 1000px;
    height: 62px;
    background: var(--page);
    box-shadow: 0 6px 12px rgba(0, 0, 0, 0.12);
  }
  .title-bar h1 {
    margin: 0;
    position: absolute;
    left: 46px;
    top: 10px;
    font-family: "Carlito", Calibri, sans-serif;
    font-style: italic;
    font-weight: 400;
    font-size: 36px;
    letter-spacing: -0.5px;
    color: var(--title);
  }
  .brand {
    position: absolute;
    left: 990px;
    top: 54px;
    display: flex;
    align-items: center;
    gap: 10px;
  }
  .brand-mark {
    width: 22px;
    height: 22px;
    background: var(--lime);
  }
  .brand-name {
    font-family: "Open Sans", Arial, sans-serif;
    font-weight: 700;
    font-size: 28px;
    color: var(--teal);
    letter-spacing: 0.5px;
  }
  .points {
    position: absolute;
    left: 58px;
    top: 254px;
    width: 500px;
    margin: 0;
    padding: 0;
    list-style: none;
  }
  .points li {
    position: relative;
    padding-left: 36px;
    font-size: 26px;
    line-height: 32px;
    margin-bottom: 20px;
  }
  .points li::before {
    content: "";
    position: absolute;
    left: 0;
    top: 5px;
    width: 20px;
    height: 20px;
  }
  .points .point-market::before { background: var(--teal); }
  .points .point-launch::before { background: var(--lime); }
  .europe-visual {
    position: absolute;
    left: 574px;
    top: 163px;
    width: 572px;
    height: 461px;
    border-radius: 10px;
    background: linear-gradient(180deg, var(--screen-light) 0%, #d6d6d6 70%, var(--screen-dark) 100%);
  }
</style>
</head>
<body>
  <main class="slide">
    <header class="title-bar">
      <h1>Investment opportunity…</h1>
    </header>
    <div class="brand">
      <span class="brand-mark"></span>
      <span class="brand-name">PLAYNOVA</span>
    </div>
    <ul class="points">
      <li class="point-market">With a market of many tens of thousands of educational establishments and countless parents, Playnova has huge potential</li>
      <li class="point-launch">To be launched in France initially, the platform will then be rolled out in the UK, Italy and Spain</li>
    </ul>
    <div class="europe-visual" role="img" aria-label="Desktop monitor showing a map of Europe with pins on France, the UK, Italy and Spain"></div>
  </main>
</body>
</html>
```